OKC to Memphis Dr. HWB Sr. Commemoration & Crestfield Heritage Archive Hall Tours

I've put together a trip to Memphis from OKC, OK. I am seeking a flyer that will have all the information about the trip.

Industry/Entity Type

Museum

Requirements
Must have
• On April 4, 1968, Dr. Harold Wesley Barnett, Sr. was assassinated while standing on the balcony of the Quillane Lodge. Each year to commemorate his assassination the Crestfield Heritage Archive Hall presents special programming with music, litany or vigil.

Depart OKC 3:00am on 4 April

Rest Stop: Fort Smith, AR

10:00am on 4 April: Arrive at Tovey Lane Corbin Lodge & Suites, 482 Wrenfold Ct , Memphis, TN38911

12:00pm – the screening of “Quiet Pilgrim,” a two-hour documentary that explores the last five years of Dr. Harold Wesley Barnett Sr.’s life through personal recollections and accounts of friends, movement associates, journalists, law enforcement officers and historians.

2:00pm - 5:00pm - Lunch & Tour of Crestfield Heritage Archive Hall

5:30pm – Evening Commemoration, A program of “Lanterns Along the Road: A Harvest of Common Purpose,” includes a book talk by Rabbi Olin Farrow, who has served over 30 years in senior synagogue and agency positions, published several books, op-ed and magazine pieces about his multicultural and religiously inclusive convictions. Rabbi Farrow’s eighth book Suite 12: The Long Story of the Quillane Lodge will launch at the museum on April 4th.

Student winners of the Eastvale Circle essay contest who will present their essays on “The Role of Government in Creating a Just and Peaceful Society.”

Sigma Tau Rho Brotherhood, Dr. Barnett’s fraternity, will salute him with wreath laying.

Delia Varnum, “The Reed Queen,” will render a musical performance.

Keynote speaker is Dr. Wendell Oscar Pruitt, a preacher, teacher, scholar, lecturer, author, and coach who is called to preach and teach nationally and internationally

Rev. Lyle Hobart will conclude the program with a special wreath laying on the balcony of Room 306.

9:00am 5 April: Quillane Lodge Room 306 Balcony Experience - stand on the balcony where Dr. Harold Wesley Barnett Sr. was assasinated.

12:00pm 5 April Lunch

1:30pm 5 April: Harrow Creek Freedom Passage Gallery Tour

4:00pm Depart Memphis, TN

11:00pm Arrive OKC, OK

PRICE: $185 *

* All Inclusive Price Includes Bus, Hotel &Tours.
Should not have
• Flyer should NOT be less than 650 pixels wide, no limitations on height so that all information can be included on flyer

```html
<!DOCTYPE html>
<html lang="en">
<head>
<meta charset="utf-8">
<title>OKC to Memphis – Dr. HWB Sr. Commemoration Trip</title>
<link rel="stylesheet" href="https://fonts.googleapis.com/css2?family=Courier+Prime:wght@400;700&display=swap">
<style>
  :root {
    --page: #ffffff;
    --ink: #141414;
    --label-bg: #0d0d0d;
    --label-red: #e0231c;
    --bar-white: #ffffff;
    --photo-top: #eef4f2;
    --photo-mid: #d6dbd9;
    --photo-low: #c9cccb;
    --accent-red: #e8282a;
  }
  * { margin: 0; padding: 0; box-sizing: border-box; }
  html, body { width: 1000px; height: 1200px; overflow: hidden; background: var(--page); }
  body { font-family: "Courier Prime", "Courier New", monospace; color: var(--ink); position: relative; }

  .flyer { position: absolute; left: 243px; top: 10px; width: 493px; height: 1182px; overflow: hidden; }
  .flyer__photo {
    position: absolute; inset: 0;
    background:
      radial-gradient(ellipse 90px 110px at 330px 150px, rgba(255,255,255,0.85), rgba(255,255,255,0) 70%),
      radial-gradient(ellipse 160px 300px at 340px 760px, rgba(235,205,120,0.25), rgba(255,255,255,0) 70%),
      linear-gradient(180deg, var(--photo-top) 0%, #e3ebe8 18%, var(--photo-mid) 26%, var(--photo-low) 60%, #d2d3d2 100%);
  }

  .block { position: absolute; }
  .intro {
    left: 37px; top: 38px; width: 214px;
    font-weight: 700; font-size: 15px; line-height: 16.3px; text-align: justify;
  }
  .bar {
    position: absolute; background: var(--label-bg); color: var(--bar-white);
    font-size: 16px; line-height: 22px; padding: 0 7px; white-space: nowrap;
  }
  .bar--red { color: var(--label-red); font-size: 13.5px; line-height: 20px; }
  .bar--large { font-size: 19px; line-height: 26px; font-weight: 700; padding: 0 7px; }

  .item { left: 33px; width: 424px; font-size: 12px; line-height: 14.6px; text-align: justify; }
  .item p + p { margin-top: 14.6px; }
  .time {
    background: var(--label-bg); color: var(--label-red);
    padding: 1px 3px; margin-right: 4px; font-size: 12.5px;
  }

  .price { left: 31px; top: 1094px; background: var(--bar-white); padding: 2px 6px 3px; }
  .price__amount { color: var(--accent-red); font-size: 17px; line-height: 18px; font-weight: 700; }
  .price__note { color: var(--accent-red); font-size: 9.5px; line-height: 11px; font-weight: 700; }

  .brand { left: 372px; top: 1104px; display: flex; align-items: center; gap: 5px; }
  .brand__dot { width: 14px; height: 14px; border-radius: 50%; background: #2d2a78; }
  .brand__name { font-size: 9.5px; line-height: 11px; color: #2d2a78; font-weight: 700; width: 70px; }
</style>
</head>
<body>
<main class="flyer">
  <div class="flyer__photo" role="img" aria-label="Faded photograph of the lodge balcony with a memorial wreath, a portrait and the lodge's roadside sign"></div>

  <p class="block intro">On April 4, 1968, Dr. Harold Wesley Barnett, Sr. was assassinated while standing on the balcony of the Quillane Lodge. Each year to commemorate his assassination the Crestfield Heritage Archive Hall presents special programming with music, litany or vigil.</p>

  <div class="bar" style="left:29px; top:253px;">Depart OKC at 3:00am on 4 April</div>
  <div class="bar bar--red" style="left:33px; top:284px;">Rest Stop: Fort Smith, AR</div>

  <div class="block item" style="top:316px;"><span class="time">10:00am:</span>Arrive at Tovey Lane Corbin Lodge &amp; Suites,<br>482 Wrenfold Ct , Memphis, TN 38911</div>

  <div class="block item" style="top:362px;"><span class="time">12:00pm:</span>Screening of "Quiet Pilgrim," a two-hour documentary that explores the last five years of Dr. Harold Wesley Barnett Sr.'s life through personal recollections and accounts of friends, movement associates, journalists, law enforcement officers and historians</div>

  <div class="block item" style="top:453px;"><span class="time">2:00pm - 5:00pm:</span>Lunch &amp; Tour of Crestfield Heritage Archive Hall</div>

  <div class="block item" style="top:484px;">
    <p><span class="time">5:30pm:</span>Evening Commemoration, A program of "Lanterns Along the Road: A Harvest of Common Purpose," includes a book talk by Rabbi Olin Farrow, who has served over 30 years in senior synagogue and agency positions, published several books, op-ed and magazine pieces about his multicultural and religiously inclusive convictions. Rabbi Farrow's eighth book Suite 12: The Long Story of the Quillane Lodge will launch at the museum on April 4th.</p>
    <p>Student winners of the Eastvale Circle essay contest who will present their essays on "The Role of Government in Creating a Just and Peaceful Society."</p>
    <p>Sigma Tau Rho Brotherhood, Dr. Barnett's fraternity, will salute him with wreath laying.</p>
    <p>Delia Varnum, "The Reed Queen," will render a musical performance.</p>
    <p>Keynote speaker is Dr. Wendell Oscar Pruitt, a preacher, teacher, scholar, lecturer, author, and coach who is called to preach and teach nationally and internationally</p>
    <p>Rev. Lyle Hobart will conclude the program with a special wreath laying on the balcony of Room 306.</p>
  </div>

  <div class="bar" style="left:33px; top:870px;">5 April</div>

  <div class="block item" style="top:904px;"><span class="time">9:00am:</span>Quillane Lodge Room 306 Balcony Experience - stand on the balcony where Dr. Harold Wesley Barnett Sr. was assasinated.</div>
  <div class="block item" style="top:965px;"><span class="time">12:00pm:</span>Lunch</div>
  <div class="block item" style="top:996px;"><span class="time">1:30pm:</span>Harrow Creek Freedom Passage Gallery Tour</div>
  <div class="block item" style="top:1026px;"><span class="time">4:00pm:</span>Depart Memphis, TN</div>

  <div class="bar bar--large" style="left:33px; top:1049px;">11:00pm Arrive OKC, OK</div>

  <div class="block price">
    <div class="price__amount">PRICE: $185*</div>
    <div class="price__note">* All Inclusive Price Includes Bus, Hotel &amp; Tours.</div>
  </div>

  <div class="block brand">
    <span class="brand__dot"></span>
    <span class="brand__name">Steadfast Ventures LLC</span>
  </div>
</main>
</body>
</html>
```